Need Business Cards for my Business

email address: rkpmarlowhollowworks@vendrimail.com
web address: rkpmarlowhollowworks.net
Slogan: We offer various QVN licenses
Rowland K. Pemberly
Please stick with colors of Company Logo
would like the card to be more of the color example of the logo.
If you need PDF copy of logo email me at the above account.
Creative control rests with you.

Industry/Entity Type

Business

Contact Information for Business Card

I am a minimalist, but would like something to pop and stand out amongst other cards, make it memorable.

Font styles to use
Serif
Decorative
Script

```html
<!DOCTYPE html>
<html lang="en">
<head>
<meta charset="utf-8">
<title>RKP Hollow Works — Business Card</title>
<link rel="stylesheet" href="https://fonts.googleapis.com/css2?family=Lato:wght@400;700;900&display=swap">
<style>
  :root {
    --backdrop: #c6c6c6;
    --card-light: #f6f5f3;
    --brand-red: #e0262d;
    --brand-red-deep: #c22031;
    --brand-blue: #2a6db3;
    --ink: #222222;
    --white: #ffffff;
  }
  html, body {
    margin: 0;
    padding: 0;
    width: 1200px;
    height: 786px;
    overflow: hidden;
    background: var(--backdrop);
    font-family: "Lato", Arial, sans-serif;
  }
  .canvas {
    position: relative;
    width: 1200px;
    height: 786px;
  }
  .card {
    position: absolute;
    top: 234px;
    height: 284px;
    box-sizing: border-box;
  }
  .card-front {
    left: 60px;
    width: 524px;
    background: var(--card-light);
  }
  .card-back {
    left: 630px;
    width: 508px;
    background: linear-gradient(180deg, #e8282d 0%, var(--brand-red-deep) 100%);
    display: flex;
    align-items: center;
    justify-content: center;
  }
  .brand-mark {
    position: absolute;
    left: 40px;
    top: 98px;
    margin: 0;
    font-size: 52px;
    font-weight: 900;
    color: var(--brand-blue);
    letter-spacing: 1px;
  }
  .contact {
    position: absolute;
    left: 222px;
    right: 20px;
    top: 62px;
    color: var(--ink);
  }
  .person-name {
    margin: 0;
    font-size: 21px;
    font-weight: 700;
    color: var(--brand-red);
    line-height: 1.1;
  }
  .person-title {
    margin: 1px 0 0;
    font-size: 13.5px;
    line-height: 1.2;
  }
  .details {
    list-style: none;
    margin: 32px 0 0;
    padding: 0;
    font-size: 13.5px;
    line-height: 19px;
  }
  .details li {
    display: flex;
    align-items: center;
    gap: 7px;
    white-space: nowrap;
  }
  .details svg {
    width: 15px;
    height: 13px;
    flex: none;
  }
  .slogan {
    margin: 10px 0 0 2px;
    font-size: 15px;
  }
  .company-name {
    margin: 0;
    font-size: 38px;
    font-weight: 900;
    color: var(--white);
    letter-spacing: 2px;
    text-align: center;
    line-height: 1.1;
  }
</style>
</head>
<body>
<main class="canvas">
  <section class="card card-front" aria-label="Card front">
    <p class="brand-mark">RKP</p>
    <div class="contact">
      <h1 class="person-name">Rowland K. Pemberly</h1>
      <p class="person-title">Managing Director</p>
      <ul class="details">
        <li>
          <svg viewBox="0 0 16 14" aria-hidden="true"><path fill="var(--brand-red)" d="M1 5c0-3 3-4 7-4s7 1 7 4l-3 1-1-2H5L4 6 1 5zM3 7h10l1 6H2z"/></svg>
          <span>555-014-2876</span>
        </li>
        <li>
          <svg viewBox="0 0 16 12" aria-hidden="true"><rect x="0.5" y="0.5" width="15" height="11" fill="var(--brand-red)"/><path d="M1 1l7 6 7-6M1 11l5-5M15 11l-5-5" stroke="#fff" fill="none"/></svg>
          <span>rkpmarlowhollowworks@vendrimail.com</span>
        </li>
        <li>
          <svg viewBox="0 0 16 16" aria-hidden="true"><g fill="none" stroke="var(--brand-red)" stroke-width="1.4"><circle cx="8" cy="8" r="7"/><ellipse cx="8" cy="8" rx="3" ry="7"/><path d="M1 8h14M2.5 4.5h11M2.5 11.5h11"/></g></svg>
          <span>www.rkpmarlowhollowworks.net</span>
        </li>
      </ul>
      <p class="slogan">We offer various QVN licenses</p>
    </div>
  </section>
  <section class="card card-back" aria-label="Card back">
    <p class="company-name">RKP HOLLOW WORKS</p>
  </section>
</main>
</body>
</html>
```